Hadley & Partners, LLC Business Card 2016

We need a new business card design for a very important trade show coming up.

We are a compliance Consulting Firm. Our clients are stock brokerage firms and investment advisers.

I would like our logo on both sides of the card.

Info in the front of the card shold include:

Logo
First & Last Name
Title
Office #
Cell #
Email
Company Address (42 W. Calloway St., Suite 300 Larkmont, CA 91417

Back of the card should include the logo and url: www.hadleypartnersgroup.com

Target Market(s)

Stock Brokerage Firms and Investment Advisers

Industry/Entity Type

Financial Service

Contact Information for Business Card

Marcus J. Pellew
President
42 W. Calloway St., Suite 300
Pasadena, CA 91417
O 626.555.0147 ext. 204
C 818.555.0193
Email: marcus@hadleypartnersgroup.com
www.hadleypartnersgroup.com

Requirements
Nice to have
• The back of the card could be black with the logo with the white letters.
• I do want the front of the card to at least have the color logo with the black "Hadley & Partners Lettering.

```html
<!DOCTYPE html>
<html lang="en">
<head>
<meta charset="utf-8">
<title>Hadley &amp; Partners — Business Card</title>
<link rel="stylesheet" href="https://fonts.googleapis.com/css2?family=Cinzel:wght@400&family=Crimson+Text:wght@400;600&display=swap">
<style>
  :root {
    --stage: #e9e6e2;
    --card-white: #ffffff;
    --brand-red: #b3141b;
    --brand-red-light: #e0392f;
    --brand-red-dark: #8e0d12;
    --wave-grey: #9aa2a8;
    --wave-grey-dark: #5f6870;
    --ink: #1d1d1d;
    --muted: #555a5e;
    --back-light: #b9bfc3;
    --back-dark: #4c5760;
    --paper-text: #ffffff;
  }
  * { box-sizing: border-box; margin: 0; padding: 0; }
  html, body { width: 1200px; height: 450px; overflow: hidden; }
  body {
    background: var(--stage);
    position: relative;
    font-family: "Crimson Text", Georgia, serif;
  }
  .card {
    position: absolute;
    top: 68px;
    height: 337px;
    border-radius: 26px;
    overflow: hidden;
    box-shadow: 0 6px 16px rgba(0,0,0,.25);
  }
  /* Front */
  .card--front { left: 38px; width: 520px; background: var(--card-white); }
  .card__waves { position: absolute; inset: 0; width: 100%; height: 100%; }
  .brand { position: absolute; display: flex; align-items: center; }
  .brand__mark { display: block; background: var(--brand-red); }
  .brand__name { font-family: "Cinzel", "Times New Roman", serif; font-weight: 400; white-space: nowrap; }
  .card--front .brand { left: 24px; top: 44px; }
  .card--front .brand__mark { width: 48px; height: 48px; margin-right: 14px; }
  .card--front .brand__name { font-size: 27px; color: var(--ink); }
  .holder { position: absolute; left: 30px; top: 160px; }
  .holder__name { font-size: 18px; font-weight: 600; color: var(--brand-red); line-height: 1.2; }
  .holder__title { font-size: 14px; color: var(--muted); line-height: 1.3; }
  .contacts {
    position: absolute; right: 22px; top: 160px;
    list-style: none; text-align: right; color: var(--paper-text);
    font-size: 15.5px; line-height: 1.25;
  }
  .contacts li { display: flex; justify-content: flex-end; align-items: flex-start; gap: 8px; margin-bottom: 6px; }
  .contacts li.gap { margin-top: 12px; }
  .contacts svg { width: 13px; height: 13px; margin-top: 3px; flex: none; fill: var(--paper-text); }
  /* Back */
  .card--back {
    left: 595px; width: 543px;
    background: linear-gradient(100deg, var(--back-light) 0%, #8c959c 55%, var(--back-dark) 100%);
  }
  .card--back .brand { left: 44px; top: 118px; }
  .card--back .brand__mark { width: 72px; height: 72px; margin-right: 20px; }
  .card--back .brand__name { font-size: 33px; color: var(--paper-text); }
  .card--back .url { position: absolute; left: 150px; top: 206px; font-size: 15px; color: var(--paper-text); }
</style>
</head>
<body>
  <section class="card card--front">
    <svg class="card__waves" viewBox="0 0 520 337" preserveAspectRatio="none" aria-hidden="true">
      <defs>
        <linearGradient id="redBand" x1="0" y1="1" x2="1" y2="0">
          <stop offset="0" stop-color="var(--brand-red-light)"/>
          <stop offset=".5" stop-color="var(--brand-red)"/>
          <stop offset="1" stop-color="var(--brand-red-dark)"/>
        </linearGradient>
        <linearGradient id="greyBand" x1="0" y1="0" x2="1" y2="0">
          <stop offset="0" stop-color="var(--wave-grey)"/>
          <stop offset="1" stop-color="var(--wave-grey-dark)"/>
        </linearGradient>
      </defs>
      <path d="M0,260 C140,275 250,250 330,190 C400,140 460,112 520,105 L520,128 C460,134 410,160 340,210 C260,268 150,292 0,285 Z" fill="url(#greyBand)"/>
      <path d="M0,300 C150,305 260,275 340,215 C410,165 465,140 520,132 L520,337 L0,337 Z" fill="url(#redBand)"/>
      <path d="M120,322 C230,312 290,285 330,250" fill="none" stroke="#ffffff" stroke-opacity=".45" stroke-width="1.5"/>
    </svg>

    <div class="brand">
      <span class="brand__mark"></span>
      <span class="brand__name">Hadley &amp; Partners</span>
    </div>

    <div class="holder">
      <p class="holder__name">Your Name</p>
      <p class="holder__title">Designation</p>
    </div>

    <ul class="contacts">
      <li><svg viewBox="0 0 16 16"><path d="M3 1l3 3-2 2c1 2 3 4 5 5l2-2 3 3-2 3C6 15 1 10 0 3z"/></svg>626-555-0147</li>
      <li><svg viewBox="0 0 16 16"><path d="M4 0h8v16H4zM5.5 2v10h5V2zM7 13.5h2v1H7z"/></svg>+1-818-555-0193</li>
      <li><svg viewBox="0 0 16 16"><path d="M8 0a5 5 0 0 1 5 5c0 4-5 11-5 11S3 9 3 5a5 5 0 0 1 5-5zm0 3a2 2 0 1 0 0 4 2 2 0 0 0 0-4z"/></svg><span>42 W. Calloway St., Suite<br>300 Larkmont, CA 91417</span></li>
      <li class="gap"><svg viewBox="0 0 16 16"><path d="M0 3h16v10H0zM1.5 4.5 8 9l6.5-4.5v-.2H1.5z"/></svg>info@hadleypartnersgroup.com</li>
      <li><svg viewBox="0 0 16 16"><path d="M8 0a8 8 0 1 0 0 16A8 8 0 0 0 8 0zm0 1.5c1 1 1.8 3 2 5.7H6c.2-2.7 1-4.7 2-5.7zM1.6 7.2c.3-2.5 2-4.5 4.3-5.3-.8 1.3-1.3 3.1-1.4 5.3zm9.9 0c-.1-2.200-.6-4-1.4-5.3 2.3.8 4 2.8 4.3 5.3zM1.6 8.8h2.9c.1 2.2.6 4 1.4 5.3-2.3-.8-4-2.8-4.3-5.3zm4.4 0h4c-.2 2.7-1 4.7-2 5.7-1-1-1.8-3-2-5.7zm5.5 0h2.9c-.3 2.5-2 4.5-4.3 5.3.8-1.3 1.3-3.1 1.4-5.3z"/></svg>www.hadleypartnersgroup.com</li>
    </ul>
  </section>

  <section class="card card--back">
    <div class="brand">
      <span class="brand__mark"></span>
      <span class="brand__name">Hadley &amp; Partners</span>
    </div>
    <p class="url">www.hadleypartnersgroup.com</p>
  </section>
</body>
</html>
```